Tot Petal Product Label for Tear-Free Head-to-Toe Wash

Need a bottle label design for a new line of natural products targeting infants and children. Products are Pediatrician-developed and paraben-free, sulfate-free, fragrance-free, and cruelty-free. Design should be clean and have a high-end feel to it. Will need other product labels in Tot Petal line designed as well in upcoming projects.

Target Market(s)

Newborn to young elementary age children and their parents

Industry/Entity Type

Cosmetics/Beauty

Font styles to use
Other font styles liked:
• Brand fonts are Jost and Sonorous

Colors

Designer to choose colors to be used in the design.

Requirements
Must have
• Tot Petal logo, Pediatrician Developed logo, and a clean high-end feel to it. The label must fit the specialty bottle we will be using (label measurements and diagram will be provided) for the front and back of bottle only (NOT the side labels). It must include our list of ingredients (will provide once designer selected).
Nice to have
• Should stand out on the shelf of other baby products due to it's clean simplicity and high-end feel
Should not have
• too much of a "kiddie" feel to it (targeting the parents not the kids)

```html
<!DOCTYPE html>
<html lang="en">
<head>
<meta charset="utf-8">
<title>Tot Petal – Tear Free Head to Toe Wash Labels</title>
<link rel="stylesheet" href="https://fonts.googleapis.com/css2?family=Grandstander:wght@400;500&family=Jost:wght@400;500&display=swap">
<style>
  :root {
    --page: #ece5dc;
    --ink: #2b2622;
    --white: #ffffff;
    --clay-label: #c9bdb2;
    --clay-ring: #a87d63;
    --sand-label: #e2cdb0;
    --sand-ring: #a8a18c;
    --stone-label: #d5c9be;
    --sky-ring: #c9dbe1;
    --swatch-clay-top: #b58c74;
    --swatch-clay-base: #d5c8bc;
    --swatch-olive-top: #a9a38f;
    --swatch-olive-base: #e5cfae;
    --swatch-sky-top: #c6d6dc;
    --swatch-sky-base: #d6ccc2;
    --badge-line: #b9ada2;
  }
  * { box-sizing: border-box; margin: 0; padding: 0; }
  html, body { width: 833px; height: 1200px; overflow: hidden; background: var(--page); }
  .canvas { position: relative; width: 833px; height: 1200px; background: var(--page); }

  .palette { position: absolute; top: 0; left: 21px; width: 791px; height: 49px; display: flex; gap: 16px; }
  .swatch { flex: 1; display: flex; flex-direction: column; }
  .swatch__top { height: 21px; }
  .swatch__base { flex: 1; }
  .swatch--clay .swatch__top { background: var(--swatch-clay-top); }
  .swatch--clay .swatch__base { background: var(--swatch-clay-base); }
  .swatch--olive .swatch__top { background: var(--swatch-olive-top); }
  .swatch--olive .swatch__base { background: var(--swatch-olive-base); }
  .swatch--sky .swatch__top { background: var(--swatch-sky-top); }
  .swatch--sky .swatch__base { background: var(--swatch-sky-base); }

  .label-set { position: absolute; top: 138px; left: 21px; display: flex; }
  .label {
    position: relative; width: 264px; height: 379px;
    color: var(--ink); font-family: "Grandstander", "Jost", sans-serif; text-align: center;
  }
  .label--clay { background: var(--clay-label); --ring: var(--clay-ring); }
  .label--sand { background: var(--sand-label); --ring: var(--sand-ring); }
  .label--stone { background: var(--stone-label); --ring: var(--sky-ring); }

  .label__claim { position: absolute; top: 48px; left: 0; right: 0; font-size: 13px; letter-spacing: 1px; }
  .label__title { position: absolute; top: 68px; left: 0; right: 0; font-size: 27px; line-height: 25px; font-weight: 400; letter-spacing: 0.5px; }
  .brand-seal {
    position: absolute; top: 133px; left: 59px; width: 146px; height: 146px; border-radius: 50%;
    background: var(--white); border: 17px solid var(--ring);
    display: flex; align-items: center; justify-content: center;
  }
  .brand-seal__name { font-size: 17px; letter-spacing: 2px; text-transform: uppercase; white-space: nowrap; }
  .badges { position: absolute; top: 311px; left: 0; right: 0; display: flex; justify-content: center; gap: 14px; }
  .badge { width: 30px; height: 30px; border-radius: 50%; background: var(--white); border: 1px solid var(--badge-line); }
  .label__volume { position: absolute; top: 350px; left: 0; right: 0; font-family: "Jost", sans-serif; font-size: 11px; }

  .bottle-labels { position: absolute; top: 640px; left: 0; width: 833px; display: flex; justify-content: center; gap: 70px; }
  .arch-frame { width: 145px; height: 208px; overflow: hidden; border-radius: 73px 73px 0 0; }
  .arch-frame .label { transform: scale(0.55); transform-origin: 0 0; border-radius: 132px 132px 0 0; }
</style>
</head>
<body>
<main class="canvas">
  <section class="palette" aria-label="Colour palette">
    <div class="swatch swatch--clay"><div class="swatch__top"></div><div class="swatch__base"></div></div>
    <div class="swatch swatch--olive"><div class="swatch__top"></div><div class="swatch__base"></div></div>
    <div class="swatch swatch--sky"><div class="swatch__top"></div><div class="swatch__base"></div></div>
  </section>

  <section class="label-set" aria-label="Flat label variants">
    <article class="label label--clay">
      <p class="label__claim">TEAR FREE</p>
      <h1 class="label__title">HEAD TO TOE<br>WASH</h1>
      <div class="brand-seal"><span class="brand-seal__name">Tot Petal</span></div>
      <div class="badges"><span class="badge"></span><span class="badge"></span><span class="badge"></span><span class="badge"></span><span class="badge"></span></div>
      <p class="label__volume">250 ml</p>
    </article>
    <article class="label label--sand">
      <p class="label__claim">TEAR FREE</p>
      <h2 class="label__title">HEAD TO TOE<br>WASH</h2>
      <div class="brand-seal"><span class="brand-seal__name">Tot Petal</span></div>
      <div class="badges"><span class="badge"></span><span class="badge"></span><span class="badge"></span><span class="badge"></span><span class="badge"></span></div>
      <p class="label__volume">250 ml</p>
    </article>
    <article class="label label--stone">
      <p class="label__claim">TEAR FREE</p>
      <h2 class="label__title">HEAD TO TOE<br>WASH</h2>
      <div class="brand-seal"><span class="brand-seal__name">Tot Petal</span></div>
      <div class="badges"><span class="badge"></span><span class="badge"></span><span class="badge"></span><span class="badge"></span><span class="badge"></span></div>
      <p class="label__volume">250 ml</p>
    </article>
  </section>

  <section class="bottle-labels" aria-label="Arched bottle label variants">
    <div class="arch-frame">
      <article class="label label--clay">
        <p class="label__claim">TEAR FREE</p>
        <h2 class="label__title">HEAD TO TOE<br>WASH</h2>
        <div class="brand-seal"><span class="brand-seal__name">Tot Petal</span></div>
        <div class="badges"><span class="badge"></span><span class="badge"></span><span class="badge"></span><span class="badge"></span><span class="badge"></span></div>
      </article>
    </div>
    <div class="arch-frame">
      <article class="label label--sand">
        <p class="label__claim">TEAR FREE</p>
        <h2 class="label__title">HEAD TO TOE<br>WASH</h2>
        <div class="brand-seal"><span class="brand-seal__name">Tot Petal</span></div>
        <div class="badges"><span class="badge"></span><span class="badge"></span><span class="badge"></span><span class="badge"></span><span class="badge"></span></div>
      </article>
    </div>
    <div class="arch-frame">
      <article class="label label--stone">
        <p class="label__claim">TEAR FREE</p>
        <h2 class="label__title">HEAD TO TOE<br>WASH</h2>
        <div class="brand-seal"><span class="brand-seal__name">Tot Petal</span></div>
        <div class="badges"><span class="badge"></span><span class="badge"></span><span class="badge"></span><span class="badge"></span><span class="badge"></span></div>
      </article>
    </div>
  </section>
</main>
</body>
</html>
```